Free range pig farm business

We'd like a simple but elegant website for our new free range pig farm business.
Check out www.kellowridgeporkers.com.au and http://www.toravinefields.com.au/
pages:
Home
About
Shop
Contact
Target Market(s)
People who would want to find out where they could buy our pork
Industry/Entity Type
Agribusiness
Number of Pages Required
4 page
Font styles to use
Other font styles liked:
- As per our logo
Requirements
Must have
- Ability for us to update weekly with new news and photos

```html
<!DOCTYPE html>
<html lang="en">
<head>
<meta charset="utf-8">
<title>Greenhollow Pastured Pork – Free Range Pig Farm</title>
<link rel="stylesheet" href="https://fonts.googleapis.com/css2?family=Oxygen:wght@400;700&family=Hind:wght@400;500;600&display=swap">
<style>
:root{
  --cream:#f7f5f0;
  --nav:#4e3733;
  --earth:#4f4a3f;
  --earth-dark:#3d382f;
  --copper:#a0683a;
  --copper-dark:#8c5a30;
  --ink:#2f2a24;
  --text:#3a342d;
  --mist:#ebebea;
  --grass:#5c8a2e;
  --line:#b9b3a8;
}
*{margin:0;padding:0;box-sizing:border-box}
html,body{width:1200px;height:3000px;overflow:hidden}
body{position:relative;background:var(--cream);font-family:"Hind",sans-serif;color:var(--text)}
.abs{position:absolute}
h1,h2,h3,.nav a,.btn{font-family:"Oxygen",sans-serif;font-weight:700;letter-spacing:2px}

/* header */
.site-header{top:0;left:0;width:1200px;height:168px;background:var(--cream)}
.social-top{left:106px;top:68px;display:flex;gap:10px}
.social-top span{width:28px;height:28px;border-radius:50%;background:var(--ink);display:block}
.brand{left:450px;top:20px;width:300px;text-align:center}
.brand-mark{width:64px;height:64px;border-radius:50%;background:var(--grass);margin:0 auto 14px}
.brand-name{font-family:"Hind",sans-serif;font-weight:600;font-size:18px;line-height:22px;color:var(--ink);letter-spacing:.5px}
.search{left:860px;top:70px;width:250px;height:28px;display:flex;border:1px solid #d8d4cc;border-radius:3px;overflow:hidden}
.search-input{flex:1;background:#f1efea;font-size:14px;font-style:italic;color:#9b968c;padding:6px 10px;letter-spacing:1px}
.search-btn{width:82px;background:#b0706a;color:#fff;font-size:13px;font-family:"Oxygen",sans-serif;font-weight:700;display:flex;align-items:center;justify-content:center;letter-spacing:1px}

.nav{top:168px;left:0;width:1200px;height:42px;background:var(--nav);display:flex;justify-content:center;gap:50px;align-items:center}
.nav a{color:#fff;text-decoration:none;font-size:19px;letter-spacing:1px}

/* hero */
.hero{top:210px;left:0;width:1200px;height:490px;background:linear-gradient(180deg,#c9cfc2 0%,#b88a5c 30%,#c57a45 50%,#6f9a37 72%,#4e7d22 100%)}
.hero-arrow{left:26px;top:408px}
.hero-caption{left:322px;top:560px;width:540px;height:76px;background:rgba(60,50,30,.55);color:#fff;font-size:48px;display:flex;align-items:center;justify-content:center}

.cta{top:700px;left:0;width:1200px;height:258px;background:var(--earth);text-align:center}
.cta h2{color:#fff;font-size:33px;line-height:48px;padding-top:38px}
.btn{background:var(--copper);color:#fff;font-size:19px;display:flex;align-items:center;justify-content:center;letter-spacing:1px}
.cta .btn{position:absolute;left:464px;top:144px;width:266px;height:58px}

/* features */
.feature{top:996px;width:320px;text-align:center}
.feature-icon{width:162px;height:162px;border:3px solid var(--copper);border-radius:50%;margin:0 auto;display:flex;align-items:center;justify-content:center}
.feature h3{font-size:19px;color:var(--ink);margin-top:24px;letter-spacing:1px}
.feature p{font-size:16px;line-height:24px;color:var(--ink);margin-top:12px;font-weight:500}
.more{margin-top:14px;display:flex;justify-content:center;align-items:center;gap:8px;color:var(--copper-dark);font-family:"Oxygen",sans-serif;font-weight:700;font-size:20px}

/* why */
.why{top:1380px;left:0;width:1200px;height:428px;background:var(--mist)}
.why h2{position:absolute;left:114px;top:38px;font-size:34px;color:var(--ink);letter-spacing:3px}
.why p{position:absolute;left:114px;top:100px;width:710px;font-size:15.5px;line-height:26px;color:var(--ink);font-weight:500}
.why .btn{position:absolute;left:114px;top:328px;width:266px;height:58px}
.butcher{left:850px;top:1390px;width:230px;height:418px;background:linear-gradient(180deg,#dcd8d2 0%,#c8c6c2 40%,#f2f2f0 100%)}

/* products */
.products-title{top:1856px;left:0;width:1200px;text-align:center;font-size:36px;line-height:48px;color:var(--ink);letter-spacing:4px}
.product{top:1984px;width:304px;text-align:center}
.product-photo{height:230px;background:linear-gradient(135deg,#c24a4e 0%,#a82e36 45%,#e6aeb0 100%)}
.product h3{font-family:"Hind",sans-serif;font-weight:600;font-size:19px;color:var(--ink);margin-top:22px;letter-spacing:1px}
.price{font-size:18px;color:#7a746a;margin-top:4px}
.product .btn{width:152px;height:46px;margin:10px auto 0;font-size:18px}

.divider{top:2400px;left:0;width:1200px;height:2px;background:#8a857c}

/* testimonials */
.quote{top:2462px;width:312px}
.quote-box{position:relative;height:110px;background:#fff;border:1px solid #d6d2ca;border-radius:6px;padding:18px 20px 0 66px;font-size:15px;line-height:24px;color:var(--ink);font-weight:500}
.quote-mark{position:absolute;left:10px;top:-6px;font-family:Georgia,serif;font-size:96px;line-height:1;color:#d7d3cb}
.quote-tail{position:absolute;left:44px;bottom:-17px}
.quote-name{margin:34px 0 0 12px;font-size:16px;font-weight:600;color:var(--copper-dark)}

/* footer */
.footer{top:2680px;left:0;width:1200px;height:268px;background:var(--earth);color:#c9c3b8}
.footer h4{font-family:"Hind",sans-serif;font-weight:500;font-size:18px;letter-spacing:1.5px;color:#c9c3b8}
.signup{left:110px;top:44px;width:352px}
.field{font-size:14px;color:#b8b2a6;border-bottom:1px solid #8b8578;padding:14px 2px 2px}
.signup .btn{height:50px;margin-top:18px;font-size:19px}
.find{left:582px;top:44px}
.find p{font-size:15px;line-height:24px;color:#ddd7cc;font-weight:500}
.find h4{margin-bottom:14px}
.keep{left:868px;top:44px}
.keep-icons{display:flex;gap:6px;margin-top:20px}
.keep-icons span{width:40px;height:40px;border:2px solid #8f897d;border-radius:50%;display:block}
.legal{top:2948px;left:0;width:1200px;height:52px;background:var(--earth-dark);color:#fff;font-family:"Oxygen",sans-serif;font-weight:700;font-size:17px;display:flex;align-items:center;justify-content:center;letter-spacing:1px}
</style>
</head>
<body>

<header class="site-header abs">
  <div class="social-top abs" aria-label="Social links"><span></span><span></span><span></span><span></span></div>
  <div class="brand abs">
    <div class="brand-mark"></div>
    <div class="brand-name">GREENHOLLOW PASTURED PORK</div>
  </div>
  <div class="search abs"><div class="search-input">Search here</div><div class="search-btn">SEARCH</div></div>
</header>

<nav class="nav abs"><a>HOME</a><a>ABOUT US</a><a>SHOP</a><a>CONTACT US</a></nav>

<section class="hero abs" role="img" aria-label="Photo of three young free range pigs standing in green grass"></section>
<svg class="hero-arrow abs" width="18" height="30" viewBox="0 0 18 30"><path d="M18 0 L0 15 L18 30 Z" fill="#fff"/></svg>
<h1 class="hero-caption abs">FREE RANGE PIGS</h1>

<section class="cta abs">
  <h2>GET FRESH MEATS FROM THE FARM<br>TO YOUR TABLE!</h2>
  <div class="btn">CLICK HERE</div>
</section>

<section class="feature abs" style="left:102px">
  <div class="feature-icon">
    <svg width="76" height="86" viewBox="0 0 76 86" fill="none" stroke="#a0683a" stroke-width="4" stroke-linejoin="round"><path d="M10 6 L22 22 H54 L66 6 L60 28 L58 56 Q38 84 18 56 L16 28 Z"/><circle cx="28" cy="40" r="3" fill="#a0683a"/><circle cx="48" cy="40" r="3" fill="#a0683a"/><ellipse cx="38" cy="62" rx="11" ry="7"/></svg>
  </div>
  <h3>THE PIGS</h3>
  <p>Lorem ipsum dolor amet, consectetuer adipiscing elit aesent vestibulum lacus. Aenean nonum hendr.</p>
  <div class="more">CLICK HERE <svg width="40" height="24" viewBox="0 0 40 24"><path d="M0 0h9l11 12-11 12H0l11-12zM18 0h9l11 12-11 12h-9l11-12z" fill="#a0683a"/></svg></div>
</section>
<section class="feature abs" style="left:448px">
  <div class="feature-icon">
    <svg width="78" height="60" viewBox="0 0 78 60"><ellipse cx="28" cy="26" rx="24" ry="20" fill="#a0683a"/><circle cx="20" cy="26" r="7" fill="#f7f5f0"/><path d="M44 36 L62 50" stroke="#a0683a" stroke-width="7" stroke-linecap="round"/><circle cx="66" cy="50" r="5" fill="#a0683a"/><circle cx="62" cy="56" r="5" fill="#a0683a"/></svg>
  </div>
  <h3>THE PORK</h3>
  <p>Lorem ipsum dolor amet, consectetuer adipiscing elit aesent vestibulum lacus. Aenean nonum hendr.</p>
  <div class="more">CLICK HERE <svg width="40" height="24" viewBox="0 0 40 24"><path d="M0 0h9l11 12-11 12H0l11-12zM18 0h9l11 12-11 12h-9l11-12z" fill="#a0683a"/></svg></div>
</section>
<section class="feature abs" style="left:788px">
  <div class="feature-icon">
    <svg width="120" height="100" viewBox="0 0 120 100" fill="#a0683a"><circle cx="44" cy="34" r="18"/><path d="M12 100 Q14 58 44 56 Q74 58 76 100Z"/><circle cx="78" cy="40" r="16"/><path d="M50 100 Q54 62 78 60 Q104 62 108 100Z"/></svg>
  </div>
  <h3>ABOUT US</h3>
  <p>Lorem ipsum dolor amet, consectetuer adipiscing elit aesent vestibulum lacus. Aenean nonum hendr.</p>
  <div class="more">CLICK HERE <svg width="40" height="24" viewBox="0 0 40 24"><path d="M0 0h9l11 12-11 12H0l11-12zM18 0h9l11 12-11 12h-9l11-12z" fill="#a0683a"/></svg></div>
</section>

<section class="why abs">
  <h2>WHY FRESH MEAT?</h2>
  <p>Lorem ipsum dolor sit amet, consectetuer adipiscing elit. Praesent vestibulum molestie lacus. Aenean nonummy hendrerit maurisasellus porta. Fusce suscipit varius mi. Cum sociis natoque penatibus et magnis dis paent mont, nascetur ridiculus mus. Nulla dui. Fusce feugiat malesuada odio. Morbi nunc odio, gravida at, cursus nec, luctus a, lorem. Maecenas tristique orci ac sem. Duis ultricies petra magna. Donec aumsan malesuada orci. Donec sit amet eros. Lorem ipsum dolor sit amet, consectetuer adipiscit. Maentum dictum magna. Sed laoreet aliquam leo. Ut tellus dolor, dapibus eget, elementum vel, cursus eleifend, elit.</p>
  <div class="btn">CLICK HERE</div>
</section>
<div class="butcher abs" role="img" aria-label="Photo of a butcher in a white apron holding a cleaver and a cut of pork"></div>

<h2 class="products-title abs">PROVIDING FARM FRESH AND HEALTHY<br>MEAT PRODUCTS</h2>
<article class="product abs" style="left:112px">
  <div class="product-photo" role="img" aria-label="Photo of small raw pork pieces on display"></div>
  <h3>SMALL PORK PIECES</h3><div class="price">$70.00</div><div class="btn">READ MORE</div>
</article>
<article class="product abs" style="left:452px">
  <div class="product-photo" role="img" aria-label="Photo of medium raw pork cuts"></div>
  <h3>MEDIUM PORK PIECES</h3><div class="price">$90.00</div><div class="btn">READ MORE</div>
</article>
<article class="product abs" style="left:794px">
  <div class="product-photo" role="img" aria-label="Photo of a large raw pork rib rack"></div>
  <h3>LARGE PORK PIECES</h3><div class="price">$100.00</div><div class="btn">READ MORE</div>
</article>

<div class="divider abs"></div>

<blockquote class="quote abs" style="left:110px">
  <div class="quote-box"><span class="quote-mark">“</span>Lorem ipsum dolor, consecte adipiscing elit aesent lacus. Aenean nonum hendr.
    <svg class="quote-tail" width="26" height="18" viewBox="0 0 26 18"><path d="M0 0 L4 18 L24 0" fill="#fff" stroke="#d6d2ca"/><rect x="1" y="-2" width="22" height="3" fill="#fff"/></svg></div>
  <div class="quote-name">Daniel Hewitt, our customer.</div>
</blockquote>
<blockquote class="quote abs" style="left:448px">
  <div class="quote-box"><span class="quote-mark">“</span>Lorem ipsum dolor, consecte adipiscing elit aesent lacus. Aenean nonum hendr.
    <svg class="quote-tail" width="26" height="18" viewBox="0 0 26 18"><path d="M0 0 L4 18 L24 0" fill="#fff" stroke="#d6d2ca"/><rect x="1" y="-2" width="22" height="3" fill="#fff"/></svg></div>
  <div class="quote-name">Daniel Hewitt, our customer.</div>
</blockquote>
<blockquote class="quote abs" style="left:786px">
  <div class="quote-box"><span class="quote-mark">“</span>Lorem ipsum dolor, consecte adipiscing elit aesent lacus. Aenean nonum hendr.
    <svg class="quote-tail" width="26" height="18" viewBox="0 0 26 18"><path d="M0 0 L4 18 L24 0" fill="#fff" stroke="#d6d2ca"/><rect x="1" y="-2" width="22" height="3" fill="#fff"/></svg></div>
  <div class="quote-name">Daniel Hewitt, our customer.</div>
</blockquote>

<footer class="footer abs">
  <div class="signup abs">
    <h4>SIGN UP FOR UPDATES</h4>
    <div class="field">Name</div>
    <div class="field">Email</div>
    <div class="btn">SIGN UP</div>
  </div>
  <div class="find abs">
    <h4>FIND US</h4>
    <p>Your Adress<br>Freephone: +1 800 555 0142<br>Telephone: +1 800 555 0187<br>FAX: +1 800 555 0163</p>
    <p style="margin-top:6px">E-mail:- hello@greenhollowpork.com</p>
  </div>
  <div class="keep abs">
    <h4>KEEP IN TOUCH</h4>
    <div class="keep-icons"><span></span><span></span><span></span><span></span><span></span></div>
  </div>
</footer>
<div class="legal abs">© 2016 PIG FARM. PRIVACY POLICY</div>

</body>
</html>
```